The Molar Nook Dental Offices Double-Sided A5 Flyer Highlighting Strengths & All Locations.

Designs are looking good. I just feel that they're too much in terms of content. Slight change in strategy. I would like a double sided A5 Flyer that has the following:

Front Side:

1. Brand (The Molar Nook Dental Offices). Use the logo that has Dental Offices beneath the words "The Molar Nook."
2. Highlight only the following keywords: Affordable. Friendly. Experienced Dental Care. Kids Friendly. We Accept All Insurance. 0% Interest Payment Plans.
3. Dental Services: Family Dentistry, Teeth Whitening, Braces, Implants, Veneers, Sedation.

Back Side:

This is where I want to highlight how convenient The Molar Nook is. We have 15 locations and growing. So here you can use our tagline:

We're Always Close to Home! With 15 Locations and Growing.

I want to list all 15 locations with each locations address and unique number. You can find those at https://molarnookexample.com/locations
The designer that can provide all locations in a catchy, easy to read and clean design will be selected.

The base of the flyer should utilize a white background. Keep it clean. Keep it fresh.

I'm looking to stand out from all competition with something unique and different. Get creative.

Target Market(s)

Women 30-40 years of age.

Industry/Entity Type

Dental

Font styles to use
Sans Serif

Colors
86cfc6
33b8a4
00a990
f59195
fdfdfb
fdf9cf
dddddd

Requirements
Must have
• Proper brand and color elements. Use white background.
Nice to have
• Surprise me with great ideas and design.
Should not have
• Prices.

```html
<!DOCTYPE html>
<html lang="en">
<head>
<meta charset="utf-8">
<title>The Molar Nook Dental Offices – A5 Flyer</title>
<link href="https://fonts.googleapis.com/css2?family=Roboto+Condensed:wght@700&family=Raleway:wght@300;400&family=Source+Sans+3:wght@300;400;600;700&family=Chewy&display=swap" rel="stylesheet">
<style>
  :root{
    --stage:#5b4a43;
    --paper:#fdfdfb;
    --mint:#86cfc6;
    --teal:#33b8a4;
    --teal-deep:#00a990;
    --band:#1fae96;
    --head-blue:#3aa3b6;
    --logo-grey:#4e5d63;
    --ink:#2f2f33;
    --maroon:#b3223a;
    --pink:#f59195;
    --pink-hot:#e8407a;
    --navy:#1d2433;
    --cream:#fdf9cf;
    --grey:#dddddd;
  }
  *{box-sizing:border-box;margin:0;padding:0}
  html,body{width:1200px;height:842px;overflow:hidden}
  body{background:var(--stage);position:relative;font-family:"Source Sans 3",sans-serif}

  .flyer{position:absolute;top:48px;width:530px;height:752px;background:var(--paper);overflow:hidden;box-shadow:3px 4px 10px rgba(0,0,0,.45)}
  .flyer--locations{left:50px}
  .flyer--services{left:614px}

  /* Locations side */
  .hero-photo{position:absolute;left:150px;top:0;width:380px;height:212px;
    background:
      linear-gradient(90deg,var(--paper) 0%,rgba(253,253,251,0) 32%),
      radial-gradient(ellipse at 65% 45%,#e9b89a 0%,#c98f74 22%,rgba(201,143,116,0) 45%),
      linear-gradient(180deg,#a9c98a 0%,#7fae63 55%,#b9d49a 100%);}
  .offer{position:absolute;left:29px;top:28px;font-family:"Roboto Condensed",sans-serif;font-weight:700;color:var(--ink);line-height:1}
  .offer span{display:block}
  .offer__lead{font-size:35px}
  .offer__rate{font-size:29px;margin-top:3px}
  .offer__rate b{color:var(--maroon);font-size:43px;font-weight:700}
  .offer__plan{font-size:30px;margin-top:5px}
  .offer__plan + .offer__plan{margin-top:3px}

  .tagline-band{position:absolute;left:0;top:212px;width:530px;height:56px;background:var(--band);
    color:#fff;font-family:"Raleway",sans-serif;font-weight:400;text-transform:uppercase;text-align:center;
    font-size:21px;letter-spacing:1.2px;line-height:23px;padding-top:5px}

  .location-grid{position:absolute;left:25px;top:277px;display:grid;grid-template-columns:repeat(3,156px);
    grid-auto-rows:86px;column-gap:6.5px;row-gap:5.5px}
  .location{background:var(--mint);border:1.5px solid #e9f6f4;box-shadow:0 1px 2px rgba(0,0,0,.25);
    text-align:center;color:#1f2b2a;font-size:8.3px;line-height:12.6px;padding-top:1px}
  .location h3{font-weight:600;font-size:12px;line-height:18px;color:#fff;text-shadow:0 1px 1.5px rgba(0,0,0,.45);
    border-bottom:1px solid rgba(255,255,255,.55);margin:0 4px 3px}
  .location .former{font-size:7.4px;margin-bottom:2px}

  /* Services side */
  .brand{position:absolute;left:40px;top:34px;display:flex;align-items:center;gap:14px}
  .brand__dot{width:46px;height:46px;border-radius:50%;background:var(--teal)}
  .brand__name{font-family:"Raleway",sans-serif;font-weight:400;font-size:36px;line-height:1;color:var(--logo-grey)}
  .brand__place{position:absolute;left:100px;top:108px;font-family:"Raleway",sans-serif;font-size:10.5px;letter-spacing:1.3px;
    color:#6d7b80;text-transform:uppercase}

  .headline{position:absolute;left:40px;top:142px;font-weight:700;color:var(--head-blue);font-size:35px;line-height:42px;letter-spacing:-.2px}

  .portrait{position:absolute;left:230px;top:230px;width:300px;height:360px;border-top-left-radius:160px 120px;
    background:
      radial-gradient(ellipse at 48% 40%,#f0cdb6 0%,#dcae92 20%,rgba(220,174,146,0) 42%),
      radial-gradient(ellipse at 75% 30%,#8a6a52 0%,rgba(138,106,82,0) 35%),
      linear-gradient(160deg,#f7f9f4 0%,#e7ecdf 55%,#f6f7f2 100%);}
  .wave{position:absolute;left:0;top:0;width:530px;height:752px}

  .services{position:absolute;left:42px;top:322px;color:var(--head-blue)}
  .services h2{font-family:"Source Sans 3",sans-serif;font-weight:300;font-size:33px;line-height:32px;color:var(--teal)}
  .services ul{list-style:none;margin-top:28px}
  .services li{font-weight:300;font-size:18.5px;line-height:26.5px;color:#2b2b2b;display:flex;align-items:center;gap:8px}
  .services li::before{content:"";width:11px;height:11px;border-radius:50%;background:radial-gradient(circle at 35% 35%,#fbc3c5,var(--pink) 60%,#e0707a)}

  .promises{position:absolute;left:30px;top:646px;font-family:"Roboto Condensed",sans-serif;font-weight:700;font-size:29px;line-height:41px}
  .promises .insurance{color:#fff;margin-left:3px}
  .promises .plans{color:var(--navy)}

  .kids-badge{position:absolute;left:325px;top:578px;width:175px;height:132px}
  .kids-badge__text{position:absolute;left:0;top:30px;width:175px;text-align:center;font-family:"Chewy",sans-serif;
    color:#fff;font-size:27px;line-height:29px;letter-spacing:1px;text-transform:uppercase}
</style>
</head>
<body>

<section class="flyer flyer--locations">
  <div class="hero-photo" role="img" aria-label="Photo of a happy family of four playing together on grass in a sunny park"></div>
  <h1 class="offer">
    <span class="offer__lead">We Offer</span>
    <span class="offer__rate"><b>0%</b> Interest</span>
    <span class="offer__plan">Payment</span>
    <span class="offer__plan">Plans</span>
  </h1>
  <p class="tagline-band">We're always close to home!<br>With 15 locations and growing</p>

  <div class="location-grid">
    <article class="location"><h3>at Larkspur Mall</h3><p>410 Larkspur Street<br>Unit T12B (in Larkspur Mall)<br>Alderbrook ON, A1A 1A1<br>Tel: (705) 555-0101</p></article>
    <article class="location"><h3>at Brightwater Plaza</h3><p>88 Willowbend Parkway East<br>Unit 213, Brightwater Plaza<br>Fernhill ON, B2B 2B2<br>Tel: 647-555-0102</p></article>
    <article class="location"><h3>at Ashford Cross St.</h3><p class="former">Formerly Dr. Pellman &amp; Associates</p><p>57 Ashford Cross St.<br>Millbrook ON, C3C 3C3<br>Tel: (519) 555-0103</p></article>

    <article class="location"><h3>at Hollis St. W.</h3><p class="former">Formerly Bright Cove Dental – Millbrook</p><p>212 Hollis Street West<br>Unit 5A, Millbrook ON, C3D 4D4<br>Tel: (519) 555-0104</p></article>
    <article class="location"><h3>at Queenly St. E.</h3><p class="former">Formerly Riverside Family Dental</p><p>33 Queenly Street East<br>Unit 8, Pinecrest ON, D5E 5E5<br>Tel: (289) 555-0105</p></article>
    <article class="location"><h3>at Cedar Grove Rd.</h3><p class="former">Formerly Cedar Grove Dental</p><p>1800 Cedar Grove Road<br>Unit 7, Westvale ON, E6F 6F6<br>Tel: (647) 555-0106</p></article>

    <article class="location"><h3>at Northgate College Blvd</h3><p class="former">Formerly Bright Cove Dental</p><p>100 Northgate College Blvd<br>Unit 103, Westvale,<br>ON E6G 7G7. Tel: (647) 555-0107</p></article>
    <article class="location"><h3>at Palomar Rd.</h3><p class="former">Formerly Palomar Dental</p><p>3040 Palomar Road, Unit 102,<br>Lakeview ON, F7H 8H8<br>Tel: (647) 555-0108</p></article>
    <article class="location"><h3>at Dorran Rd. E.</h3><p class="former">Formerly Maplefield Dental</p><p>3530 Dorran Road East, Unit 203<br>Lakeview ON, F7J 9J9<br>Tel: (647) 555-0109</p></article>

    <article class="location"><h3>at Midtown Pkwy Mall</h3><p>377 Brookhaven Rd. E. #121<br>Midtown Parkway Mall (2nd Floor)<br>Lakeview ON, F7K 1K1<br>Tel: 647-555-0110</p></article>
    <article class="location"><h3>at Tamarack Road</h3><p>4920 Tamarack Rd.<br>Unit # 2, Lakeview,<br>Ontario F7L 2L2<br>Tel: 647-555-0111</p></article>
    <article class="location"><h3>at Eastwood Plaza</h3><p class="former">Formerly Eastwood Dental</p><p>2131 Lorimer Ave. East, Unit 5<br>Ridgeview ON, G8M 3M3<br>Tel: (647) 555-0112</p></article>

    <article class="location"><h3>at Kingsley Square</h3><p class="former">Formerly Kingsley Square Dental</p><p>4463A Kingsley Road<br>Ridgeview ON, G8N 4N4<br>Tel: (647) 555-0113</p></article>
    <article class="location"><h3>at Kendall Rd.</h3><p>1910 Kendall Road, Unit 7<br>Ridgeview ON,<br>G8P 5P5<br>Tel: (647) 555-0114</p></article>
    <article class="location"><h3>at Stony Brook / Harbourton</h3><p>521 Hwy 9, Unit #3<br>Stony Brook ON, H9R 6R6<br>Tel: 289-555-0115</p></article>
  </div>
</section>

<section class="flyer flyer--services">
  <div class="brand">
    <span class="brand__dot"></span>
    <span class="brand__name">The Molar Nook</span>
  </div>
  <p class="brand__place">Dental Office at Larkspur Mall</p>

  <h1 class="headline">Affordable, Friendly,<br>Experienced Dental Care</h1>

  <div class="portrait" role="img" aria-label="Photo of a smiling woman resting her arms on a white sofa in a bright room"></div>

  <svg class="wave" viewBox="0 0 530 752" aria-hidden="true">
    <path d="M0,530 C70,600 170,640 300,620 C400,605 470,560 530,520" fill="none" stroke="#cfe9e3" stroke-width="1.5"/>
    <path d="M0,545 C80,610 180,640 310,628 C410,615 475,575 530,540" fill="none" stroke="#9fd6cb" stroke-width="2"/>
    <path d="M0,565 C90,625 190,650 320,640 C420,630 480,600 530,570 L530,752 L0,752 Z" fill="var(--band)"/>
    <path d="M210,290 C300,230 420,230 470,250" fill="none" stroke="#ffffff" stroke-width="3" opacity=".8"/>
  </svg>

  <div class="services">
    <h2>Dental<br>Services</h2>
    <ul>
      <li>Family Dentistry</li>
      <li>Teeth Whitening</li>
      <li>Braces</li>
      <li>Implants</li>
      <li>Veneers</li>
      <li>Sedation</li>
    </ul>
  </div>

  <div class="kids-badge">
    <svg viewBox="0 0 175 132" width="175" height="132" aria-hidden="true">
      <ellipse cx="88" cy="66" rx="82" ry="60" fill="var(--pink)"/>
      <ellipse cx="88" cy="66" rx="84" ry="62" fill="none" stroke="var(--pink-hot)" stroke-width="2.5"/>
    </svg>
    <p class="kids-badge__text">Kids<br>Friendly</p>
  </div>

  <div class="promises">
    <p class="insurance">We Accept All Insurance</p>
    <p class="plans">0% Interest Payment Plans</p>
  </div>
</section>

</body>
</html>
```